Brisk Canopy Builders needs a product brochure

We need a new flyer for our Porch Nook Lounge. Here is some of the copy your will need.
"Turn your back yard into the ultimate entertianment venue with the stunning Porch Nook Lounge!"
"Entertain family & friends in your very own back yard!"
"Available with or without solar and comes in a variety of colors"
"The Porch Nook Lounge measures 5' deep by 10' wide and is 9'-6" at it's highest point"
"Constructed with treated 4x4's, primed then painted with Garrick Pellman best exterior paint for years of care free enjoyment. Also, Farley Dunmore Steadfast shingles are dimensional, have a 25 year warranty and are rated for 150 mph winds!"
"TV Mount included. Shelves and TV are sold separately"
There also needs to be a box where we can add the price into later. The price can change from time to time due to material cost fluctuation.

```html
<!DOCTYPE html>
<html lang="en">
<head>
<meta charset="UTF-8">
<title>Porch Nook Lounge Flyer</title>
<link href="https://fonts.googleapis.com/css2?family=Barlow+Semi+Condensed:wght@500;700;800&family=Montserrat:wght@500;800;900&display=swap" rel="stylesheet">
<style>
  :root {
    --orange: #f7a823;
    --green: #2f9a3d;
    --green-dark: #1f6f2b;
    --ink: #1b1b1b;
    --white: #ffffff;
    --text-dark: #262626;
  }
  * { margin: 0; padding: 0; box-sizing: border-box; }
  html, body { width: 720px; height: 1200px; overflow: hidden; background: var(--white); }
  .flyer { position: relative; width: 720px; height: 1200px; overflow: hidden; background: var(--white); font-family: "Montserrat", sans-serif; }
  .backdrop { position: absolute; left: 0; top: 0; }
  .brand { position: absolute; left: 40px; top: 96px; width: 250px; display: flex; align-items: center; gap: 12px; z-index: 2; }
  .brand-dot { flex: none; width: 26px; height: 26px; border-radius: 50%; background: var(--green); }
  .brand-name { font-family: "Barlow Semi Condensed", sans-serif; font-weight: 800; font-size: 36px; line-height: 1.02; color: var(--orange); text-transform: uppercase; letter-spacing: 0.5px; }
  .headline { position: absolute; left: 46px; top: 330px; font-family: "Barlow Semi Condensed", sans-serif; text-transform: uppercase; line-height: 1.02; }
  .headline .plain { display: block; color: var(--white); font-weight: 500; font-size: 25px; }
  .headline .accent { display: block; color: var(--orange); font-weight: 800; font-size: 40px; }
  .headline .accent.small { font-size: 31px; }
  .detail-shot { position: absolute; width: 138px; height: 138px; border-radius: 50%; border: 5px solid var(--white); box-shadow: 0 3px 8px rgba(0,0,0,.3); }
  .shot-bottles { left: 22px; top: 620px; background: radial-gradient(circle at 50% 40%, #a0572a, #2a1a12); }
  .shot-host { left: 171px; top: 620px; background: radial-gradient(circle at 50% 45%, #8a8a80, #3a3a34); }
  .shot-shelf { left: 320px; top: 620px; background: radial-gradient(circle at 45% 55%, #c98a48, #1d2a3a); }
  .price-box { position: absolute; left: 457px; top: 612px; width: 214px; height: 250px; border-radius: 10px; background: linear-gradient(180deg, var(--green), var(--green-dark)); box-shadow: 0 10px 10px -6px rgba(0,0,0,.45); text-align: center; padding-top: 30px; }
  .price-label { font-family: "Montserrat", sans-serif; font-weight: 900; font-size: 30px; line-height: 1.08; color: var(--white); text-transform: uppercase; }
  .price-value { margin-top: 8px; font-family: "Barlow Semi Condensed", sans-serif; font-weight: 800; font-size: 60px; color: var(--orange); }
  .tagline { position: absolute; left: 47px; top: 796px; font-family: "Barlow Semi Condensed", sans-serif; font-weight: 700; font-size: 29px; line-height: 1.3; color: var(--text-dark); text-transform: uppercase; }
  .footer-band { position: absolute; left: 0; top: 1060px; width: 720px; height: 140px; background: var(--orange); }
  .features { position: absolute; left: 45px; top: 893px; width: 627px; height: 246px; background: linear-gradient(180deg, var(--green), var(--green-dark)); border-radius: 4px; display: flex; padding: 26px 18px; color: var(--white); font-size: 15.5px; line-height: 1.38; }
  .features ul { list-style: none; }
  .features .col-left { width: 300px; padding-right: 14px; border-right: 1px dashed var(--orange); }
  .features .col-right { flex: 1; padding-left: 16px; }
  .features li { position: relative; padding-left: 30px; margin-bottom: 16px; }
  .features li svg { position: absolute; left: 0; top: 2px; }
  .contact { position: absolute; left: 0; top: 1158px; width: 720px; display: flex; justify-content: center; align-items: center; font-family: "Barlow Semi Condensed", sans-serif; font-weight: 700; font-size: 17px; color: var(--ink); }
  .contact span { display: flex; align-items: center; gap: 6px; padding: 0 12px; }
  .contact span + span { border-left: 1px solid var(--ink); }
</style>
</head>
<body>
<main class="flyer">
  <svg class="backdrop" width="720" height="700" viewBox="0 0 720 700">
    <defs>
      <linearGradient id="photoTone" x1="0" y1="0" x2="0" y2="1">
        <stop offset="0" stop-color="#6f8a3c"/>
        <stop offset="0.35" stop-color="#b1703a"/>
        <stop offset="0.7" stop-color="#2b2b2b"/>
        <stop offset="1" stop-color="#9a9a96"/>
      </linearGradient>
    </defs>
    <rect x="0" y="0" width="720" height="700" fill="url(#photoTone)" role="img" aria-label="Photo of the Porch Nook Lounge backyard bar with solar roof, TV, shelves and bar stools"/>
    <path d="M0,250 C140,320 330,300 400,200 C360,340 380,480 440,560 C320,640 140,665 0,650 Z" fill="var(--ink)"/>
    <path d="M0,0 H390 C420,170 300,300 0,295 Z" fill="var(--orange)"/>
    <path d="M0,0 H370 C395,160 280,280 0,280 Z" fill="var(--white)"/>
    <path d="M0,650 C210,672 420,640 580,575 C650,545 695,520 720,500 V700 H0 Z" fill="var(--orange)"/>
    <path d="M0,665 C210,688 420,660 585,595 C655,565 700,540 720,525 V700 H0 Z" fill="var(--white)"/>
  </svg>

  <div class="brand">
    <span class="brand-dot"></span>
    <span class="brand-name">Brisk Canopy<br>Builders</span>
  </div>

  <h1 class="headline">
    <span class="plain">Turn your</span>
    <span class="accent">Back yard</span>
    <span class="plain">into the ultimate</span>
    <span class="accent small">Entertainment</span>
    <span class="plain">venue with the</span>
    <span class="accent">Stunning</span>
    <span class="accent small">Porch Nook Lounge!</span>
  </h1>

  <div class="detail-shot shot-bottles" role="img" aria-label="Close-up of bottle shelf and glass rack"></div>
  <div class="detail-shot shot-host" role="img" aria-label="Guests enjoying drinks at the lounge"></div>
  <div class="detail-shot shot-shelf" role="img" aria-label="Close-up of wooden shelf detail"></div>

  <div class="price-box">
    <div class="price-label">Price<br>starting<br>at just</div>
    <div class="price-value">$75,000</div>
  </div>

  <h2 class="tagline">Entertain family &amp; friends<br>in your very own back yard!</h2>

  <div class="footer-band"></div>

  <section class="features">
    <ul class="col-left">
      <li><svg width="18" height="18" viewBox="0 0 18 18"><circle cx="9" cy="9" r="9" fill="var(--orange)"/><path d="M5 9.5l3 3 5-6" stroke="#fff" stroke-width="2" fill="none"/></svg>Available with or without solar and comes in a variety of colors</li>
      <li><svg width="18" height="18" viewBox="0 0 18 18"><circle cx="9" cy="9" r="9" fill="var(--orange)"/><path d="M5 9.5l3 3 5-6" stroke="#fff" stroke-width="2" fill="none"/></svg>The Porch Nook Lounge measures 5' deep by 10' wide and is 9'-6" at it's highest point</li>
      <li><svg width="18" height="18" viewBox="0 0 18 18"><circle cx="9" cy="9" r="9" fill="var(--orange)"/><path d="M5 9.5l3 3 5-6" stroke="#fff" stroke-width="2" fill="none"/></svg>TV Mount included. Shelves and TV are sold separately</li>
    </ul>
    <ul class="col-right">
      <li><svg width="18" height="18" viewBox="0 0 18 18"><circle cx="9" cy="9" r="9" fill="var(--orange)"/><path d="M5 9.5l3 3 5-6" stroke="#fff" stroke-width="2" fill="none"/></svg>Constructed with treated 4x4's, primed then painted with Garrick Pellman best exterior paint for years of care free enjoyment. Also, Farley Dunmore Steadfast shingles are dimensional, have a 25 year warranty and are rated for 150 mph winds!</li>
    </ul>
  </section>

  <footer class="contact">
    <span><svg width="15" height="15" viewBox="0 0 24 24"><path d="M6.6 10.8a15 15 0 006.6 6.6l2.2-2.2c.3-.3.7-.4 1-.2 1.1.4 2.3.6 3.6.6.6 0 1 .4 1 1V20c0 .6-.4 1-1 1A17 17 0 013 4c0-.6.4-1 1-1h3.5c.6 0 1 .4 1 1 0 1.3.2 2.5.6 3.6.1.3 0 .7-.2 1z" fill="none" stroke="currentColor" stroke-width="2"/></svg>555-318-0472</span>
    <span><svg width="15" height="15" viewBox="0 0 24 24" fill="none" stroke="currentColor" stroke-width="2"><circle cx="12" cy="12" r="10"/><path d="M2 12h20M12 2c3 3 3 17 0 20M12 2c-3 3-3 17 0 20"/></svg>www.BriskCanopyBuilders.com</span>
    <span><svg width="16" height="14" viewBox="0 0 24 20" fill="none" stroke="currentColor" stroke-width="2"><rect x="1" y="1" width="22" height="18"/><path d="M1 1l11 10L23 1"/></svg>hello@BriskCanopyBuilders.com</span>
  </footer>
</main>
</body>
</html>
```